Wedding "Survival Kit" Bag label

I saw a "Wedding Week Survival Kit" that someone create via this site. They had the same design printed twice (facing opposite directions) on the front of the oversized card and then folded it to top off a bag filled with goodies for their guests. That is what I'm looking to go as well as need help with the design for the card. We are getting married in the Riviera Maya on August 2nd, 2015 and both love very modern designs. Our names are Meris Dolvane and Otto Flemmerik.

We would like the label to say something like "Wedding Survival Kit" and have some type of cool, abs tract logo that includes our first names, the location and maybe even the date. Feel free to visit our wedding website for inspiration: www.merisandotto.example

Industry/Entity Type

Wedding

Font styles to use
Other font styles liked:
• Chalkduster or anything fun

Requirements
Must have
• A fun flare to it!! Bright colors are encouraged!
Should not have
• Traditional boring fonts, or basic design

```html
<!DOCTYPE html>
<html lang="en">
<head>
<meta charset="utf-8">
<title>Mexico Wedding Week Survival Kit – Bag Label</title>
<link rel="stylesheet" href="https://fonts.googleapis.com/css2?family=Oswald:wght@500&family=Yellowtail&family=Londrina+Solid:wght@900&family=Chewy&family=Delius&display=swap">
<style>
  :root {
    --paper: #f1e6d3;
    --teal: #1f7f8c;
    --green: #7cb342;
    --yellow: #f2b705;
    --orange: #f07a1f;
    --red: #d9333f;
    --berry: #a8306a;
    --plum: #b04a86;
    --ink: #2a2a2a;
    --oval: #f6ee8c;
    --dots: #1ea0e0;
    --frame: #e0566a;
  }
  html, body { margin: 0; padding: 0; overflow: hidden; background: var(--paper); }
  .label {
    position: relative;
    width: 1200px;
    height: 779px;
    background: var(--paper);
    overflow: hidden;
    font-family: "Oswald", sans-serif;
  }
  .fold-line { position: absolute; left: 0; top: 0; }
  .half {
    position: absolute;
    left: 0;
    width: 1200px;
    height: 389.5px;
  }
  .half--top { top: 0; transform: rotate(180deg); }
  .half--bottom { top: 389.5px; }
  .frame { position: absolute; left: 0; top: 0; }

  .slogan-row {
    position: absolute;
    left: 88px;
    width: 1030px;
    display: flex;
    gap: 22px;
    font-size: 25px;
    letter-spacing: 2px;
    line-height: 1;
    white-space: nowrap;
  }
  .slogan-row--inner { top: 30px; }
  .slogan-row--outer { top: 341px; }
  .half--top .slogan-row--outer { transform: rotate(180deg); }

  .slogan-col {
    position: absolute;
    top: 78px;
    height: 240px;
    writing-mode: vertical-rl;
    font-size: 25px;
    letter-spacing: 2px;
    line-height: 1;
    text-align: center;
    white-space: nowrap;
  }
  .slogan-col--left { left: 44px; transform: rotate(180deg); color: var(--red); }
  .slogan-col--right { left: 1130px; color: var(--green); }

  .edge-note {
    position: absolute;
    writing-mode: vertical-rl;
    font-size: 13px;
    letter-spacing: 1.5px;
    color: var(--red);
    white-space: nowrap;
  }
  .edge-note--venue { left: 6px; top: 80px; height: 250px; transform: rotate(180deg); text-align: center; }
  .edge-note--date { left: 1176px; top: 80px; height: 250px; text-align: center; }
  .heart { color: var(--red); }

  .c-teal { color: var(--teal); }
  .c-green { color: var(--green); }
  .c-yellow { color: var(--yellow); }
  .c-orange { color: var(--orange); }
  .c-red { color: var(--red); }

  .place-title {
    position: absolute;
    left: 118px;
    top: 92px;
    margin: 0;
    font-family: "Londrina Solid", sans-serif;
    font-weight: 900;
    font-size: 136px;
    line-height: 1;
    letter-spacing: 2px;
  }
  .event-title {
    position: absolute;
    left: 230px;
    top: 212px;
    margin: 0;
    font-family: "Yellowtail", cursive;
    font-weight: 400;
    font-size: 70px;
    line-height: 1;
    color: var(--teal);
  }
  .kit-badge {
    position: absolute;
    left: 732px;
    top: 80px;
    width: 212px;
    height: 116px;
    border-radius: 50%;
    background: var(--oval);
    border: 5px dotted var(--dots);
    box-sizing: border-box;
    display: flex;
    align-items: center;
    justify-content: center;
    text-align: center;
    font-family: "Chewy", cursive;
    font-size: 38px;
    line-height: 0.95;
    color: var(--berry);
  }
  .couple {
    position: absolute;
    left: 700px;
    width: 300px;
    top: 202px;
    margin: 0;
    text-align: center;
    font-family: "Delius", sans-serif;
    font-size: 40px;
    color: var(--ink);
  }
  .couple .amp { color: var(--plum); }
  .wedding-date {
    position: absolute;
    left: 776px;
    top: 252px;
    display: flex;
    gap: 3px;
  }
  .date-dot {
    width: 46px;
    height: 46px;
    border-radius: 50%;
    background: var(--plum);
    color: #fbe9f1;
    font-family: "Delius", sans-serif;
    font-size: 22px;
    display: flex;
    align-items: center;
    justify-content: center;
  }
</style>
</head>
<body>
<div class="label">

  <section class="half half--top" aria-label="Upside-down label face">
    <svg class="frame" width="1200" height="390" aria-hidden="true">
      <g fill="none" stroke="var(--frame)" stroke-width="2" stroke-dasharray="7 5">
        <line x1="32" y1="68" x2="1168" y2="68"/>
        <line x1="32" y1="326" x2="1168" y2="326"/>
        <line x1="76" y1="68" x2="76" y2="326"/>
        <line x1="1124" y1="68" x2="1124" y2="326"/>
        <line x1="32" y1="20" x2="32" y2="375"/>
        <line x1="1168" y1="20" x2="1168" y2="375"/>
      </g>
    </svg>
    <div class="slogan-row slogan-row--inner">
      <span class="c-teal">TOO MUCH FUN</span>
      <span class="c-orange">TOO MUCH FOOD</span>
      <span class="c-teal">TOO MUCH BOOZE</span>
      <span class="c-yellow">TOO MUCH SUN</span>
    </div>
    <div class="slogan-row slogan-row--outer">
      <span class="c-teal">TOO MUCH BOOZE</span>
      <span class="c-yellow">TOO MUCH SUN</span>
      <span class="c-red">TOO MUCH FOOD</span>
      <span class="c-green">TOO MUCH FUN</span>
    </div>
    <div class="slogan-col slogan-col--left">TOO MUCH FUN</div>
    <div class="slogan-col slogan-col--right">TOO MUCH SUN</div>
    <div class="edge-note edge-note--venue"><span class="heart">♥</span> PALMERA COSTA RESORT, MEXICO</div>
    <div class="edge-note edge-note--date"><span class="heart">♥</span> SUNDAY, AUGUST 02, 2015</div>

    <h2 class="place-title"><span class="c-teal">M</span><span class="c-green">E</span><span class="c-red">X</span><span class="c-yellow">I</span><span class="c-orange">C</span><span class="c-red">O</span></h2>
    <p class="event-title">Wedding Week</p>
    <div class="kit-badge">SURVIVAL<br>KIT</div>
    <p class="couple">Meris <span class="amp">&amp;</span> Otto</p>
    <div class="wedding-date"><span class="date-dot">08</span><span class="date-dot">02</span><span class="date-dot">15</span></div>
  </section>

  <section class="half half--bottom" aria-label="Label face">
    <svg class="frame" width="1200" height="390" aria-hidden="true">
      <g fill="none" stroke="var(--frame)" stroke-width="2" stroke-dasharray="7 5">
        <line x1="32" y1="68" x2="1168" y2="68"/>
        <line x1="32" y1="326" x2="1168" y2="326"/>
        <line x1="76" y1="68" x2="76" y2="326"/>
        <line x1="1124" y1="68" x2="1124" y2="326"/>
        <line x1="32" y1="20" x2="32" y2="375"/>
        <line x1="1168" y1="20" x2="1168" y2="375"/>
      </g>
    </svg>
    <div class="slogan-row slogan-row--inner">
      <span class="c-teal">TOO MUCH BOOZE</span>
      <span class="c-yellow">TOO MUCH SUN</span>
      <span class="c-orange">TOO MUCH FOOD</span>
      <span class="c-green">TOO MUCH FUN</span>
    </div>
    <div class="slogan-row slogan-row--outer">
      <span class="c-teal">TOO MUCH FUN</span>
      <span class="c-orange">TOO MUCH FOOD</span>
      <span class="c-red">TOO MUCH BOOZE</span>
      <span class="c-teal">TOO MUCH SUN</span>
    </div>
    <div class="slogan-col slogan-col--left">TOO MUCH FUN</div>
    <div class="slogan-col slogan-col--right">TOO MUCH SUN</div>
    <div class="edge-note edge-note--venue"><span class="heart">♥</span> PALMERA COSTA RESORT, MEXICO</div>
    <div class="edge-note edge-note--date"><span class="heart">♥</span> SUNDAY, AUGUST 02, 2015</div>

    <h1 class="place-title"><span class="c-teal">M</span><span class="c-green">E</span><span class="c-red">X</span><span class="c-yellow">I</span><span class="c-orange">C</span><span class="c-red">O</span></h1>
    <p class="event-title">Wedding Week</p>
    <div class="kit-badge">SURVIVAL<br>KIT</div>
    <p class="couple">Meris <span class="amp">&amp;</span> Otto</p>
    <div class="wedding-date"><span class="date-dot">08</span><span class="date-dot">02</span><span class="date-dot">15</span></div>
  </section>

  <svg class="fold-line" width="1200" height="779" aria-hidden="true">
    <line x1="30" y1="389.5" x2="1170" y2="389.5" stroke="var(--teal)" stroke-width="2" stroke-dasharray="7 5"/>
  </svg>
</div>
</body>
</html>
```